依頼詳細
ソフトウェア開発会社で新卒採用に使用できる会社案内を依頼させていただきます。
基本的には会社のホームページとジョブテラに掲載している情報を会社案内にして
いただきますが、パワーポイントで概要も出来ておりますので依頼者には展開いたします。
サイズ
A4
ページ数
4ページ
希望イメージ
シンプル 複雑
単色 カラフル
暗い 明るい
日常 高級
遊び心 厳粛
未来的 伝統的
女性的 男性的
希望する色
青系、水色系
納品ファイル
補足説明
納品ファイルは添付ファイルと同じようなパワーポイントを希望します。
ご質問にも回答させていただきましたが、サイズはA4とありますが、
2つ折りにしたらA4を想定しています。
納品物はパワーポイントで文字などは自由に編集できる状態でお願いします。
■ 選んだ理由

1.添付ファイルの資料だけでなく、当社のHPをよく見ていただき提案していただいた点です。
2.短期間で複数のパターンをご提案をいただいたことです。

■ 提案者全員のお礼・コメント

この度は弊社の会社案内のデザインのコンペに多数のご応募をありがとうございました。
ご提案いただきましたデザインはどれも素敵なものばかりでしたが、最終的には選んだ
理由に記載させていただいたとおりでございます。
また機会がございましたらよろしくお願いいたします。

```html
<!DOCTYPE html>
<html lang="ja">
<head>
<meta charset="UTF-8">
<title>NORTHWAVE SYSTEMS 会社案内</title>
<link rel="stylesheet" href="https://fonts.googleapis.com/css2?family=Barlow:wght@500&family=Barlow+Condensed:wght@600&family=Noto+Sans+JP:wght@400;500&display=swap">
<style>
  :root {
    --blue-deep: #1a2f8f;
    --blue-mid: #2f5fd0;
    --blue-light: #5d9cf0;
    --sky-pale: #a9cdf7;
    --brand-blue: #1f3f9e;
    --ink: #2b2b3a;
    --white: #ffffff;
  }
  * { margin: 0; padding: 0; box-sizing: border-box; }
  html, body { width: 846px; height: 1200px; overflow: hidden; background: var(--white); }
  .cover {
    position: relative;
    width: 846px;
    height: 1200px;
    background: var(--white);
  }
  .hero {
    position: absolute;
    left: 0; top: 0;
    width: 846px;
    height: 849px;
    background:
      radial-gradient(ellipse at 30% 40%, rgba(120, 180, 250, 0.55), transparent 55%),
      radial-gradient(ellipse at 80% 15%, rgba(40, 70, 180, 0.6), transparent 60%),
      linear-gradient(160deg, var(--blue-deep) 0%, var(--blue-mid) 45%, var(--blue-light) 75%, var(--sky-pale) 100%);
  }
  .skyline {
    position: absolute;
    left: 0; bottom: 0;
    width: 846px;
    height: 200px;
    background: linear-gradient(180deg, rgba(170, 205, 245, 0) 0%, rgba(190, 218, 250, 0.55) 60%, rgba(225, 238, 252, 0.8) 100%);
  }
  .headline {
    position: absolute;
    top: 320px;
    width: 100%;
    text-align: center;
    font-family: "Barlow", sans-serif;
    font-weight: 500;
    font-size: 60px;
    letter-spacing: 3px;
    color: var(--white);
  }
  .tagline {
    position: absolute;
    top: 410px;
    width: 100%;
    text-align: center;
    font-family: "Noto Sans JP", sans-serif;
    font-weight: 500;
    font-size: 17px;
    line-height: 37px;
    letter-spacing: 4px;
    color: var(--white);
  }
  .brand {
    position: absolute;
    top: 1022px;
    width: 100%;
    text-align: center;
    font-family: "Barlow Condensed", sans-serif;
    font-weight: 600;
    font-size: 42px;
    letter-spacing: 1px;
    color: var(--brand-blue);
  }
  .doc-title {
    position: absolute;
    top: 1094px;
    width: 100%;
    text-align: center;
    font-family: "Noto Sans JP", sans-serif;
    font-weight: 500;
    font-size: 16px;
    letter-spacing: 6px;
    color: var(--ink);
  }
</style>
</head>
<body>
  <main class="cover">
    <section class="hero" role="img" aria-label="青と水色の三角形が重なる幾何学パターンの背景">
      <div class="skyline" role="img" aria-label="白い線画で描かれた高層ビルが並ぶ都市の街並み"></div>
    </section>
    <h1 class="headline">Like to job.</h1>
    <p class="tagline">好きな仕事を通して<br>夢の実現と社会に<br>貢献を目指しています。</p>
    <p class="brand">NORTHWAVE SYSTEMS</p>
    <p class="doc-title">会社案内</p>
  </main>
</body>
</html>
```